Layla Karim Haddad Desert Fragrances

All our perfumes are non-alcoholic and water based. We want to have a design that would have some Arabic calligraphy, arabesque etc. We would be the label theme u design for all our scents. Of course, the scent flavor would changed. We will also use the pattern on the packaging of the scent as well. Something along the lines of this brand: http://veridocrest.example/en/.
Label size: Length 6"; Height 5"

Target Market(s)

middle east (Kuwait, UAE, Saudi Arabia);

Requirements
Must have
• 1. Flavor Name (editable)
• 2. Quantity 240 ml / 100 ml (editable)
• 3. Flavor Description (editable. each flavor has its own unique description)
• 4. Logo (place where we can display our logo. Logo file submitted.)
• 5. Company Name (editable. I should be able to edit this field too.)
Nice to have
• Flavor name in English and Arabic. You don't have to do any translation. Just make a space for us so that we can type-in the Arabic name. It wud be good to place the Arabic flavor name right below the English one.
Should not have
• images of animals, people

```html
<!DOCTYPE html>
<html lang="en">
<head>
<meta charset="utf-8">
<title>Oud Cedar – Layla Karim Haddad Desert Fragrances</title>
<link rel="stylesheet" href="https://fonts.googleapis.com/css2?family=EB+Garamond:ital,wght@0,400;0,700;1,400&family=Inter:wght@200;300&display=swap">
<style>
  :root {
    --brown-deep: #4a3430;
    --brown-mid: #7a3440;
    --rose: #e8325a;
    --rose-soft: #ec3d62;
    --ink: #4a2a2c;
    --white: #ffffff;
  }
  * { margin: 0; padding: 0; box-sizing: border-box; }
  html, body { width: 1000px; height: 1200px; overflow: hidden; }
  body { font-family: "EB Garamond", Georgia, serif; }

  .label {
    position: relative;
    width: 1000px;
    height: 1200px;
    overflow: hidden;
  }
  .label__rose-pattern {
    position: absolute;
    inset: 0;
    background: linear-gradient(180deg,
      var(--brown-deep) 0%,
      #5a3333 18%,
      var(--brown-mid) 32%,
      #c22f50 46%,
      var(--rose) 58%,
      var(--rose-soft) 100%);
  }

  .ribbon {
    position: absolute;
    left: 156px;
    top: 174px;
    width: 188px;
    height: 373px;
  }
  .ribbon svg { position: absolute; inset: 0; }
  .ribbon__name {
    position: absolute;
    left: 0;
    right: 0;
    top: 92px;
    text-align: center;
    color: var(--white);
    font-family: "Inter", "Helvetica Neue", Arial, sans-serif;
  }
  .ribbon__name-main {
    display: block;
    font-weight: 200;
    font-size: 68px;
    line-height: 76px;
    letter-spacing: 4px;
  }
  .ribbon__name-sub {
    display: block;
    margin-top: 14px;
    font-weight: 300;
    font-size: 23px;
    letter-spacing: 7px;
    padding-left: 7px;
  }

  .brand-mark {
    position: absolute;
    left: 140px;
    top: 820px;
    width: 226px;
    text-align: center;
    color: var(--white);
    font-size: 25px;
    line-height: 30px;
    font-weight: 400;
  }
  .brand-mark__dot {
    display: block;
    width: 14px;
    height: 14px;
    margin: 0 auto 12px;
    border-radius: 50%;
    background: var(--white);
  }

  .credits {
    position: absolute;
    left: 530px;
    top: 700px;
    width: 446px;
    text-align: center;
    color: var(--ink);
  }
  .credits__heading { font-size: 22px; line-height: 30px; }
  .credits__creator { font-size: 22px; line-height: 30px; }
  .credits__origin { font-size: 25px; line-height: 30px; margin-top: 34px; }
  .credits__story {
    margin: 14px auto 0;
    width: 430px;
    font-style: italic;
    font-size: 12.6px;
    line-height: 19px;
    text-transform: uppercase;
  }

  .volume {
    position: absolute;
    left: 100px;
    top: 1054px;
    width: 300px;
    text-align: center;
    color: var(--white);
    font-weight: 700;
    font-size: 36px;
  }
  .tagline {
    position: absolute;
    top: 1124px;
    width: 320px;
    text-align: center;
    color: var(--white);
    font-weight: 700;
    font-size: 22px;
  }
  .tagline--left { left: 90px; }
  .tagline--right { left: 590px; }
</style>
</head>
<body>
<main class="label">
  <div class="label__rose-pattern" role="img" aria-label="Outline rose line pattern over a brown to rose-pink gradient"></div>

  <div class="ribbon">
    <svg width="188" height="373" viewBox="0 0 188 373" aria-hidden="true">
      <defs>
        <linearGradient id="ribbonFill" x1="0" y1="0" x2="0" y2="1">
          <stop offset="0" stop-color="#e8325a"/>
          <stop offset="0.35" stop-color="#cf2f55"/>
          <stop offset="0.7" stop-color="#6e3338"/>
          <stop offset="1" stop-color="#4a3430"/>
        </linearGradient>
      </defs>
      <polygon points="0,0 188,0 188,373 94,329 0,373" fill="url(#ribbonFill)"/>
    </svg>
    <h1 class="ribbon__name">
      <span class="ribbon__name-main">OUD</span>
      <span class="ribbon__name-sub">CEDAR</span>
    </h1>
  </div>

  <div class="brand-mark">
    <span class="brand-mark__dot"></span>
    Layla Karim Haddad Desert Fragrances
  </div>

  <section class="credits">
    <p class="credits__heading">CREATED BY:</p>
    <p class="credits__creator">Layla Karim Haddad</p>
    <p class="credits__origin">PRODUCT OF KUWAIT</p>
    <p class="credits__story">The Layla Karim Haddad built by Julien Marchetti in 2003 in Paris. After spending many years in Saudi Arabia, where he created perfumes for the royal family, he came back in Paris to present his astonishing oriental creations to the occidental world.</p>
  </section>

  <p class="volume">240 ml</p>
  <p class="tagline tagline--left">Non-Alcoholic Fragrance</p>
  <p class="tagline tagline--right">Non-Alcoholic Fragrance</p>
</main>
</body>
</html>
```